3.5" x 11" Door Hanger Design - Residential Roofing Company

We are looking for a double-sided door hanger that we can hang on the doors of prospects. This door hanger would have some brief information about our company, a phone number, website, and then the services that we offer. I don't know that it will have enough room for a lot of pictures, but feel free to use those from the marketing brochure if you think it'll work and I can get you the original as needed.
I have uploaded our certifications, logo, and then our current marketing brochure. The design should be cohesive with our marketing brochure, but doesn't have to match it perfectly.
Lastly, attached is the template that we are planning to print off of. This has a tear off portion at the bottom for a business card for a sales rep. The size of the overall door hanger will be 3.5" x 11", with the bottom 2.5" being the tear off business card with the salesman's information. I'll get you the sales reps information during the final design phase, but we will need name, title, phone number, email, business address, business website, list of services, and then the words "AZ ROC 562071" all on that small portion as well so if they tear it off they still have all the info.

```html
<!DOCTYPE html>
<html lang="en">
<head>
<meta charset="utf-8">
<title>Sedona Ridge Roofing – Door Hanger</title>
<link href="https://fonts.googleapis.com/css2?family=Oswald:wght@500;700&family=Roboto+Slab:wght@400;700;800&display=swap" rel="stylesheet">
<style>
  :root{
    --page:#e4e4e4;
    --charcoal:#2a2a2c;
    --orange:#f26722;
    --white:#ffffff;
    --text-soft:#d9d9d9;
    --sky-top:#9fb3c8;
    --sky-bottom:#e6ecf2;
    --house:#6e6a64;
    --rule:#6a6a6e;
  }
  *{box-sizing:border-box;margin:0;padding:0}
  html,body{width:1200px;height:3156px;overflow:hidden;background:var(--page)}
  body{position:relative;font-family:"Roboto Slab",Georgia,serif;color:var(--white)}
  .hanger{position:absolute;top:730px;width:540px;height:1697px;background:var(--charcoal);border-radius:8px;overflow:hidden;box-shadow:0 4px 14px rgba(0,0,0,.25)}
  .hanger--front{left:40px}
  .hanger--back{left:620px}
  .hang-hole{position:absolute;top:40px;left:195px;width:150px;height:150px;border-radius:50%;background:var(--page);z-index:5}
  .abs{position:absolute;left:0;width:100%}
  .photo{position:absolute}
  .heading{font-family:"Oswald",Arial,sans-serif;text-transform:uppercase;text-align:center}

  /* front */
  .front-hero{top:0;height:600px;background:linear-gradient(180deg,var(--sky-top),var(--sky-bottom) 55%,#b9a890 75%,var(--house))}
  .brand-name{top:230px;font-size:46px;font-weight:700;color:var(--charcoal);text-align:center}
  .roof-band{top:540px;height:100px}
  .tagline{top:640px;font-family:"Roboto Slab",Georgia,serif;text-transform:uppercase;text-align:center}
  .tagline .lead{font-size:52px;font-weight:800;color:var(--orange);line-height:1}
  .tagline .rest{font-size:46px;font-weight:800;line-height:1.1}
  .tagline-rule{top:808px;left:40px;width:460px;height:2px;background:var(--orange)}
  .roof-types{top:820px;font-family:"Oswald",Arial,sans-serif;font-size:24px;letter-spacing:2px;color:var(--white);text-align:center}
  .roof-types span{color:var(--orange);margin:0 6px}
  .intro{top:880px;padding:0 36px;font-size:19px;line-height:1.45;color:var(--text-soft);text-align:center}
  .offices{top:1065px;padding:0 40px;font-size:19px;line-height:1.45;color:var(--text-soft);text-align:center}
  .front-photo{left:0;top:1180px;width:540px;height:110px;background:linear-gradient(180deg,#a9bfd4,#dfe6ec 40%,#8d8a85 70%,#5f6a5a)}
  .front-chevron{top:1150px;height:70px}
  .phone-bar{top:1270px;height:62px;background:var(--white);color:var(--charcoal);display:flex;align-items:center;justify-content:center;gap:14px;font-family:"Oswald",Arial,sans-serif;font-size:46px;font-weight:700}
  .web-bar{top:1332px;height:38px;background:var(--orange);font-size:22px;font-weight:700;text-align:center;line-height:38px}
  .tear-line{top:1380px;left:12px;width:516px;border-top:3px dashed var(--rule)}
  .card-lines{top:1420px;padding:0 70px}
  .card-lines div{height:2px;background:var(--rule);margin-bottom:50px}

  /* back */
  .services-title{top:225px}
  .services-title .kicker{font-family:"Roboto Slab",Georgia,serif;font-size:30px;font-weight:700;color:var(--orange);text-transform:uppercase}
  .services-title .main{font-size:34px;font-weight:500;letter-spacing:1px}
  .service-grid{top:320px;padding:0 26px;display:grid;grid-template-columns:1fr 1fr;column-gap:28px;row-gap:28px}
  .service h3{font-size:23px;font-weight:700;text-align:center;line-height:1.15}
  .service h3 em{display:block;font-style:normal;color:var(--orange)}
  .service p{margin-top:10px;font-size:17px;line-height:1.42;color:var(--text-soft);text-align:center}
  .coating-note{top:855px;font-size:21px;font-weight:700;font-style:italic;color:var(--orange);text-align:center}
  .sample-row{top:895px;display:flex;justify-content:center;gap:18px}
  .sample{width:108px;height:108px;border-radius:50%;border:3px solid var(--white)}
  .sample--metal{background:linear-gradient(135deg,#9aa2a8,#5e656b)}
  .sample--tile{background:linear-gradient(135deg,#e08a4f,#a9491f)}
  .sample--flat{background:linear-gradient(135deg,#d6d6d6,#8f9396)}
  .sample--shingle{background:linear-gradient(135deg,#5b5b5e,#2f2f33)}
  .back-photo{left:0;top:1040px;width:540px;height:140px;background:linear-gradient(180deg,#b7c9d9,#e3e8ec 35%,#8a8782 65%,#55604f)}
  .back-chevron{top:1022px;height:60px}
  .call-band{top:1180px;height:48px;background:var(--orange);font-size:34px;font-weight:700;line-height:48px}
  .back-phone{top:1232px;height:62px;display:flex;align-items:center;justify-content:center;gap:14px;font-family:"Oswald",Arial,sans-serif;font-size:46px;font-weight:700;color:var(--orange)}
  .contact{top:1320px;font-size:19px;line-height:1.5;color:var(--text-soft);text-align:center}
  .license{top:1480px;font-family:"Oswald",Arial,sans-serif;font-size:34px;font-weight:700;color:var(--orange);text-align:center}
  .back-foot{top:1560px;height:100px;display:flex;align-items:center;justify-content:space-between;padding:0 34px}
  .badge{width:86px;height:86px;border-radius:50%;background:var(--white)}
  .badge--green{background:#3aa34a}
  .badge--shield{border-radius:10px;background:#2f5d9e}
  .foot-name{font-size:26px;font-weight:700;color:var(--white)}
</style>
</head>
<body>

<section class="hanger hanger--front" aria-label="Door hanger front">
  <div class="hang-hole"></div>
  <div class="photo abs front-hero" role="img" aria-label="Photo of a stone and timber house with a tile roof under a blue sky"></div>
  <div class="abs brand-name">Sedona Ridge Roofing</div>

  <svg class="abs roof-band" viewBox="0 0 540 100" preserveAspectRatio="none" aria-hidden="true">
    <polygon points="0,100 270,18 540,100" fill="var(--charcoal)"/>
    <polyline points="0,92 270,10 540,92" fill="none" stroke="var(--orange)" stroke-width="12"/>
  </svg>

  <div class="abs tagline">
    <div class="lead">Quality</div>
    <div class="rest">Roofing<br>You Can Trust</div>
  </div>
  <div class="abs tagline-rule"></div>
  <div class="abs roof-types">TILE<span>|</span>METAL<span>|</span>SHINGLE<span>|</span>LOW SLOPE</div>

  <p class="abs intro">At Sedona Ridge Roofing, we have established ourselves as a leading provider of residential roofing installation services throughout Arizona. With thousands of successful installations of tile, metal, shingle, and flat roofs, we've built a solid reputation based on quality, integrity, and unmatched customer service.</p>
  <p class="abs offices">With office locations in Prescott and Glendale, we are ready to serve your roofing needs across the state.</p>

  <div class="photo front-photo" role="img" aria-label="Photo of a finished home with a new grey roof"></div>
  <svg class="abs front-chevron" viewBox="0 0 540 70" preserveAspectRatio="none" aria-hidden="true">
    <polygon points="0,0 540,0 540,66 270,8 0,66" fill="var(--charcoal)"/>
    <polyline points="0,66 270,8 540,66" fill="none" stroke="var(--orange)" stroke-width="8"/>
  </svg>

  <div class="abs phone-bar">
    <svg width="40" height="40" viewBox="0 0 24 24" aria-hidden="true"><circle cx="12" cy="12" r="12" fill="var(--orange)"/><path d="M8.2 6.5l1.7-.4 1 2.6-1.2 1a7 7 0 003 3l1-1.2 2.6 1-.4 1.7c-4.2.6-8.3-3.5-7.7-7.7z" fill="#fff"/></svg>
    928-555-0147
  </div>
  <div class="abs web-bar">www.sedonaridgeroofing.com</div>

  <div class="abs tear-line"></div>
  <div class="abs card-lines"><div></div><div></div><div></div><div></div><div></div></div>
</section>

<section class="hanger hanger--back" aria-label="Door hanger back">
  <div class="hang-hole"></div>

  <div class="abs heading services-title">
    <div class="kicker">Premier Residential</div>
    <div class="main">Roofing Services</div>
  </div>

  <div class="abs service-grid">
    <article class="service">
      <h3>Standing Seam<em>Metal Roofing</em></h3>
      <p>Sedona Ridge Roofing installs all types of metal roofing systems, including standing seam metal, metal panels, metal shingles and more.</p>
    </article>
    <article class="service">
      <h3>Tiles<em>Roofing</em></h3>
      <p>Sedona Ridge Roofing installs all types of tile roofing, including concrete tile, clay tile, metal tile and more.</p>
    </article>
    <article class="service">
      <h3>Flat Roof<em>Systems</em></h3>
      <p>Sedona Ridge Roofing installs many types of flat roofing, including membrane roofing, modified bitumen, applied coatings and more.</p>
    </article>
    <article class="service">
      <h3>Asphalt Shingle<em>Roofing</em></h3>
      <p>Sedona Ridge Roofing installs dimensional asphalt shingles, including Ridgeline HD shingles and more.</p>
    </article>
  </div>

  <div class="abs coating-note">Also provides professional roof coating services</div>
  <div class="abs sample-row">
    <div class="sample sample--metal" role="img" aria-label="Close-up photo of a metal roof"></div>
    <div class="sample sample--tile" role="img" aria-label="Close-up photo of clay roof tiles"></div>
    <div class="sample sample--flat" role="img" aria-label="Close-up photo of a flat roof membrane"></div>
    <div class="sample sample--shingle" role="img" aria-label="Close-up photo of asphalt shingles"></div>
  </div>

  <div class="photo back-photo" role="img" aria-label="Aerial photo of a house with a new roof"></div>
  <svg class="abs back-chevron" viewBox="0 0 540 60" preserveAspectRatio="none" aria-hidden="true">
    <polygon points="0,0 540,0 540,56 270,8 0,56" fill="var(--charcoal)"/>
    <polyline points="0,56 270,8 540,56" fill="none" stroke="var(--orange)" stroke-width="8"/>
  </svg>

  <div class="abs heading call-band">Call Us Today</div>
  <div class="abs back-phone">
    <svg width="40" height="40" viewBox="0 0 24 24" aria-hidden="true"><circle cx="12" cy="12" r="12" fill="var(--orange)"/><path d="M8.2 6.5l1.7-.4 1 2.6-1.2 1a7 7 0 003 3l1-1.2 2.6 1-.4 1.7c-4.2.6-8.3-3.5-7.7-7.7z" fill="#fff"/></svg>
    928-555-0147
  </div>

  <div class="abs contact">
    hello@sedonaridgeroofing.com<br>
    www.sedonaridgeroofing.com<br>
    210 W Pine Ave, Prescott AZ 86301<br>
    Monday-Friday: 8am-5pm
  </div>
  <div class="abs license">AZ ROC 562071</div>

  <div class="abs back-foot">
    <div class="badge badge--shield" role="img" aria-label="Certification badge"></div>
    <div class="foot-name">Sedona Ridge Roofing</div>
    <div class="badge badge--green" role="img" aria-label="Certification badge"></div>
  </div>
</section>

</body>
</html>
```